Health and natural healing website needs label design for pink salt

I need a label for my Himalayan pink salt. It needs to have my logo on there somewhere, website address: www.velbrinwellness.example, email: info@velbrinwellness.example, 750g, fine grade

The salt packaging is a brown striped kraft-look stand alone bag, resealable and has a rectangular window on the front where the pink salt is visible.

The space above the window is where I would like to have the label. The label needs to measure 8cm wide by 5cm tall. I think an oval shaped label would work best?

The label needs to be simple yet effective. It should stand out from the crowd yet be easy enough to read.

My logo needs to be attractive and professional. I think green works best for health but am open to other ideas. Maybe a tree?

Target Market(s)

People wanting to get healthy

Industry/Entity Type

Health And Wellness

Logo Text

Velbrin Wellness

Colors
33b8a4
00a990
86cfc6
9bcb3c
acd036
cadf82

Requirements
Must have
• website address: www.velbrinwellness.example
• email: info@velbrinwellness.example
Nice to have
• a tree? for the logo, not the salt label...

```html
<!DOCTYPE html>
<html lang="en">
<head>
<meta charset="utf-8">
<title>Himalayan Pink Salt Label – Velbrin Wellness</title>
<link rel="stylesheet" href="https://fonts.googleapis.com/css2?family=Oswald:wght@400;500;600&display=swap">
<style>
  :root {
    --page-bg: #ecebe6;
    --label-light: #d3e6a0;
    --label-mid: #bcd779;
    --frame-green: #5c8a2e;
    --logo-green: #1f5a2a;
    --logo-text: #ffffff;
    --ink-dark: #4a5334;
    --ink-soft: #5f6845;
    --art-light: rgba(236, 242, 214, 0.55);
    --art-fade: rgba(236, 242, 214, 0);
  }
  * { margin: 0; padding: 0; box-sizing: border-box; }
  html, body {
    width: 1200px; height: 900px; overflow: hidden;
    background: var(--page-bg);
    font-family: "Oswald", "Arial Narrow", sans-serif;
  }
  .canvas {
    position: relative; width: 1200px; height: 900px;
    display: flex; align-items: center; justify-content: center;
  }
  .label {
    position: relative; width: 960px; height: 636px;
    background: linear-gradient(180deg, var(--label-light), var(--label-mid));
    border: 3px solid var(--frame-green);
    box-shadow: 0 8px 24px rgba(0,0,0,0.15);
    overflow: hidden;
  }
  .label-frame {
    position: absolute; inset: 12px;
    border: 2px solid var(--frame-green);
    opacity: 0.7; pointer-events: none; z-index: 3;
  }
  .mountain-art {
    position: absolute; left: 0; right: 0; top: 150px; bottom: 0;
    z-index: 1;
    background: linear-gradient(180deg, var(--art-fade) 0%, var(--art-light) 45%, var(--art-light) 100%);
  }
  .brand-mark {
    position: absolute; top: 48px; left: 50%; transform: translateX(-50%);
    z-index: 4;
    display: flex; align-items: center; gap: 16px;
    background: var(--logo-green);
    padding: 12px 26px 12px 20px;
    border: 3px solid var(--logo-text);
    outline: 2px solid var(--logo-green);
  }
  .brand-square { width: 40px; height: 40px; background: var(--logo-text); flex: none; }
  .brand-name {
    color: var(--logo-text); font-size: 34px; font-weight: 400; line-height: 1.05;
    display: flex; flex-direction: column;
  }
  .product {
    position: absolute; top: 225px; left: 0; right: 0; z-index: 4;
    text-align: center; color: var(--ink-dark);
  }
  .product-origin { font-size: 58px; font-weight: 500; letter-spacing: 4px; line-height: 1; }
  .product-name { font-size: 100px; font-weight: 600; letter-spacing: 5px; line-height: 1.05; margin-top: 10px; }
  .product-grade {
    font-size: 28px; font-weight: 400; letter-spacing: 2px; margin-top: 22px;
    color: var(--ink-soft);
  }
  .product-grade .mark { margin: 0 22px; }
  .product-weight { font-size: 42px; font-weight: 600; margin-top: 6px; }
  .contact {
    position: absolute; bottom: 30px; left: 0; right: 0; z-index: 4;
    display: flex; justify-content: center; gap: 120px;
    font-size: 20px; color: var(--ink-soft);
  }
</style>
</head>
<body>
<main class="canvas">
  <section class="label">
    <div class="mountain-art" role="img" aria-label="Soft illustration of a snow-capped Himalayan mountain peak"></div>
    <div class="label-frame"></div>

    <div class="brand-mark">
      <span class="brand-square"></span>
      <span class="brand-name"><span>Velbrin</span><span>Wellness</span></span>
    </div>

    <div class="product">
      <p class="product-origin">HIMALAYAN</p>
      <h1 class="product-name">PINK SALT</h1>
      <p class="product-grade"><span class="mark">∞</span>FINE GRADE<span class="mark">∞</span></p>
      <p class="product-weight">750G</p>
    </div>

    <footer class="contact">
      <span>www.velbrinwellness.example</span>
      <span>info@velbrinwellness.example</span>
    </footer>
  </section>
</main>
</body>
</html>
```